Seed Oil Safety Card for Healthy Restaurant Dining

I am seeking a design for a physical card to communicate my wife's health-related dietary restriction regarding seed oils. This card will be given to restaurant waiters to ensure her meals are prepared without seed oils, as it is a health issue and not merely a preference.
My wife cannot eat any “seed oil” or “processed oil”, including:
- Vegetable oil
- Canola oil
- Soybean oil
- Sunflower oil
- Corn oil
- Cottonseed oil
- Safflower oil
- Peanut oil
- Sesame oil
Oils that are OK for her to consume:
- Butter (most preferable)
- Extra virgin olive oil
- Avocado oil
- Coconut oil
- Ghee
- Lard
- Any other animal-based fats
Key Design Requirements:
- Clarity and speed of communication: The card should be easily read and understood by waiters, even in low-light environments, emphasizing that it's a health concern.
- Avoid common misconceptions: Ensure the design doesn't imply common dietary preferences like "vegetarian" or "no butter." Animal fats and butter are actually preferable for her!
- Preferred term: Use "seed oils" as the term to describe what she cannot eat due to her health issue.
- Trace amounts are acceptable: Communicate that it's OK to use cookware that has previously been in contact with seed oils, but not to have seed oil as an ingredient. Please suggest a concise way to convey this.
- Card dimensions: Design should be 3.5” x 2.25” (standard credit-card size on cardlomex.example). Horizontal or vertical layouts are both fine, whichever makes the message clearer.
Design Suggestions:
- Utilize bold and easy-to-read typography to communicate the main message.
- Consider incorporating relevant icons or graphics that help convey the message without adding confusion.
- Use contrasting colors to enhance readability, especially in low-light situations.
- To communicate the “trace amounts OK” part, consider phrases such as:
- "Cross-contamination acceptable"
- “Used cookware OK, no ingredient use”
- “Separate cookware not necessary”
Thank you for your assistance in creating this essential card for my wife's health and safety when dining out!

```html
<!DOCTYPE html>
<html lang="en">
<head>
<meta charset="utf-8">
<title>Seed Oil Dietary Restriction Card</title>
<link rel="stylesheet" href="https://fonts.googleapis.com/css2?family=Bebas+Neue&display=swap">
<style>
  :root {
    --canvas: #ffffff;
    --alert-red: #fb0e18;
    --alert-yellow: #ffe000;
    --footer-yellow: #fdd400;
    --orange-edge: #e4520c;
    --orange-mid: #f39a0e;
    --glow-yellow: #fde812;
    --ink: #111111;
    --safe-green-head: #5adc17;
    --safe-green-body: #8af02a;
    --safe-green-glow: #cde27e;
    --safe-ink: #1e3a0c;
    --back-label: #1b4a0b;
    --tick: #11c40e;
    --drop-dark: #e8bd00;
    --drop-light: #fbe26a;
  }
  html, body {
    margin: 0;
    padding: 0;
    width: 1200px;
    height: 1200px;
    overflow: hidden;
    background: var(--canvas);
  }
  .sheet { display: block; width: 1200px; height: 1200px; }
  .type { font-family: "Bebas Neue", "Oswald", sans-serif; }
  .side-label { font-size: 67px; }
  .side-label--front { fill: var(--alert-red); }
  .side-label--back { fill: var(--back-label); }
  .eyebrow { font-size: 34px; fill: var(--ink); letter-spacing: 9px; }
  .warning-title { font-size: 67px; fill: var(--alert-yellow); }
  .oil-list { font-size: 44px; fill: var(--ink); letter-spacing: -0.6px; }
  .trace-note { font-size: 34px; fill: var(--ink); }
  .safe-title { font-size: 58px; fill: var(--safe-ink); }
  .safe-list { font-size: 44px; fill: var(--safe-ink); letter-spacing: -0.6px; }
</style>
</head>
<body>
<svg class="sheet type" viewBox="0 0 1200 1200" xmlns="http://www.w3.org/2000/svg">
  <defs>
    <clipPath id="front-shape">
      <path d="M322 27.5 H1076 V470 A100 100 0 0 1 976 570 H232 V117.5 A90 90 0 0 1 322 27.5 Z"/>
    </clipPath>
    <clipPath id="back-shape">
      <path d="M232 619 H992 A90 90 0 0 1 1082 709 V1166 H342 A110 110 0 0 1 232 1056 Z"/>
    </clipPath>
    <radialGradient id="warning-glow" cx="0.5" cy="0.35" r="0.6">
      <stop offset="0" stop-color="var(--glow-yellow)"/>
      <stop offset="0.45" stop-color="var(--orange-mid)"/>
      <stop offset="1" stop-color="var(--orange-edge)"/>
    </radialGradient>
    <radialGradient id="safe-glow" cx="0.55" cy="0.45" r="0.55">
      <stop offset="0" stop-color="var(--safe-green-glow)"/>
      <stop offset="1" stop-color="var(--safe-green-body)"/>
    </radialGradient>
    <radialGradient id="drop-fill" cx="0.5" cy="0.7" r="0.6">
      <stop offset="0" stop-color="var(--drop-light)"/>
      <stop offset="1" stop-color="var(--drop-dark)"/>
    </radialGradient>
  </defs>

  <text class="side-label side-label--front" x="57" y="359" textLength="121" lengthAdjust="spacingAndGlyphs">FRONT</text>
  <text class="side-label side-label--back" x="74" y="911" textLength="99" lengthAdjust="spacingAndGlyphs">BACK</text>

  <!-- Front: seed oils to avoid -->
  <g class="card card--front" clip-path="url(#front-shape)">
    <rect class="card__header" x="232" y="27.5" width="844" height="126" fill="var(--alert-red)"/>
    <rect class="card__body" x="232" y="153" width="844" height="321" fill="url(#warning-glow)"/>
    <rect class="card__footer" x="232" y="474" width="844" height="96" fill="var(--footer-yellow)"/>
  </g>
  <text class="eyebrow" x="378" y="67" textLength="616" lengthAdjust="spacing">HEALTH-RELATED DIETARY RESTRICTION</text>
  <text class="warning-title" x="660" y="129" text-anchor="middle" textLength="743" lengthAdjust="spacingAndGlyphs">SEED OILS ARE NOT OK FOR CONSUMPTION</text>

  <g class="icon icon--no-oil">
    <path d="M374 159 C400 205 462 290 462 356 A88 88 0 0 1 286 356 C286 290 348 205 374 159 Z" fill="url(#drop-fill)"/>
    <circle cx="374" cy="308" r="104" fill="none" stroke="var(--alert-red)" stroke-width="31"/>
    <line x1="303" y1="253" x2="444" y2="366" stroke="var(--alert-red)" stroke-width="31"/>
  </g>

  <g class="oil-list">
    <text x="507" y="253">- VEGETABLE OIL</text>
    <text x="507" y="294">- CANOLA OIL</text>
    <text x="507" y="335">- SOYBEAN OIL</text>
    <text x="507" y="375">- SUNFLOWER OIL</text>
    <text x="507" y="416">- CORN OIL</text>
    <text x="756" y="253">- COTTONSEED OIL</text>
    <text x="756" y="294">- SAFFLOWER OIL</text>
    <text x="756" y="335">- PEANUT OIL</text>
    <text x="756" y="375">- SESAME OIL</text>
  </g>

  <g class="trace-note">
    <text x="253" y="515" textLength="366" lengthAdjust="spacingAndGlyphs">CROSS-CONTAMINATION ACCEPTABLE</text>
    <text x="646" y="517" textLength="365" lengthAdjust="spacingAndGlyphs">USED COOKWARE OK, NO INGREDIENT USE</text>
    <text x="654" y="551" text-anchor="middle" textLength="383" lengthAdjust="spacingAndGlyphs">SEPARATE COOKWARE NOT NECESSARY</text>
  </g>

  <!-- Back: oils that are fine -->
  <g class="card card--back" clip-path="url(#back-shape)">
    <rect class="card__body" x="232" y="619" width="850" height="547" fill="url(#safe-glow)"/>
    <rect class="card__header" x="232" y="619" width="850" height="126" fill="var(--safe-green-head)"/>
  </g>
  <text class="safe-title" x="361" y="703" textLength="594" lengthAdjust="spacingAndGlyphs">OILS THAT ARE OK FOR CONSUMPTION</text>

  <g class="icon icon--ok-oil">
    <path d="M362 800 C390 850 453 930 453 996 A91 91 0 0 1 271 996 C271 930 334 850 362 800 Z" fill="url(#drop-fill)"/>
    <polyline points="291,941 364,1009 450,861" fill="none" stroke="var(--tick)" stroke-width="16" stroke-linecap="round" stroke-linejoin="round"/>
  </g>

  <g class="safe-list">
    <text x="510" y="824">- BUTTER (MOST PREFERABLE)</text>
    <text x="510" y="865">- EXTRA VIRGIN OLIVE OIL</text>
    <text x="510" y="906">- AVOCADO OIL</text>
    <text x="510" y="946">- COCONUT OIL</text>
    <text x="510" y="987">- GHEE</text>
    <text x="510" y="1027">- LARD</text>
    <text x="510" y="1068">- ANY OTHER ANIMAL-BASED FATS</text>
  </g>
</svg>
</body>
</html>
```